Webdesign Chiropraktik
Zielgruppe
Amerikanische Chiropraktik
Aufgabenstellung
keine direkten vorgaben...Wir sind ein junges Team und brauchen eine moderne ansprechende Webseite...

```html
<!DOCTYPE html>
<html lang="de">
<head>
<meta charset="utf-8">
<title>Halden Praxis</title>
<link href="https://fonts.googleapis.com/css2?family=Bebas+Neue&family=Poppins:wght@400;500;600&display=swap" rel="stylesheet">
<style>
:root{
  --mint:#effbea;
  --green:#46b735;
  --ink:#2d2d2d;
  --muted:#8c978a;
  --grey:#9a9a9a;
  --white:#ffffff;
}
*{margin:0;padding:0;box-sizing:border-box}
html,body{width:1200px;height:863px;overflow:hidden;background:var(--white);font-family:'Poppins',sans-serif;color:var(--ink)}
.page{position:relative;width:1200px;height:863px}
.hero{position:absolute;left:0;top:0;width:1200px;height:611px;background:var(--mint)}
.hero-photo{position:absolute;left:0;top:0}
.brand{position:absolute;left:100px;top:21px;display:flex;align-items:center;gap:8px;font-family:'Poppins',sans-serif;font-weight:600;font-size:20px;line-height:26px;color:var(--green)}
.brand-dot{width:14px;height:14px;border-radius:50%;background:var(--green)}
.nav{position:absolute;left:373px;top:26px;display:flex;gap:27px;font-size:12px}
.nav a{color:var(--ink);text-decoration:none}
.btn{display:inline-block;background:var(--green);color:var(--white);border-radius:30px;font-weight:500;text-align:center}
.btn-top{position:absolute;left:949px;top:22px;width:151px;height:30px;line-height:30px;font-size:12px}
.hero-title{position:absolute;left:113px;top:140px;font-family:'Bebas Neue',sans-serif;font-size:84px;line-height:78px;color:var(--ink);font-weight:400}
.hero-sub{position:absolute;left:100px;top:325px;width:400px;font-size:15px;line-height:25px;color:var(--muted)}
.btn-main{position:absolute;left:100px;top:423px;width:150px;height:38px;line-height:38px;font-size:12px;box-shadow:0 14px 28px rgba(70,183,53,.18)}
.contact-link{position:absolute;left:280px;top:432px;font-size:12px;color:var(--ink);display:flex;align-items:center;gap:12px}
.contact-link span{text-decoration:underline}
.social{position:absolute;top:533px;left:100px}
.social i{position:absolute;top:0;width:37px;height:37px;border-radius:50%;background:var(--ink)}
.hotline{position:absolute;left:900px;top:523px;width:200px;height:62px;background:var(--white);border-radius:31px;box-shadow:0 18px 40px rgba(0,0,0,.07)}
.hotline-icon{position:absolute;left:11px;top:12px;width:38px;height:38px;border-radius:50%;background:var(--mint);display:flex;align-items:center;justify-content:center}
.hotline-label{position:absolute;left:58px;top:10px;font-size:11px;color:var(--green)}
.hotline-number{position:absolute;left:58px;top:27px;font-size:15px;font-weight:600;color:var(--ink)}
.intro{position:absolute;left:100px;top:680px;width:1000px}
.intro h2{font-family:'Bebas Neue',sans-serif;font-weight:400;font-size:32px;margin-left:4px;line-height:38px}
.intro .lead{font-size:15px;color:var(--grey);margin:5px 0 0 4px;line-height:22px}
.intro p.body{font-size:15px;line-height:25px;margin-top:7px;letter-spacing:-0.1px}
</style>
</head>
<body>
<div class="page">
  <header class="hero">
    <svg class="hero-photo" width="1200" height="611" role="img" aria-label="Foto: Chiropraktiker behandelt den Nacken einer liegenden Patientin">
      <defs>
        <linearGradient id="photoTone" x1="0" y1="0" x2="1" y2="1">
          <stop offset="0" stop-color="#6e6462"/>
          <stop offset=".45" stop-color="#4a3f3c"/>
          <stop offset=".75" stop-color="#2a2524"/>
          <stop offset="1" stop-color="#1b1919"/>
        </linearGradient>
      </defs>
      <path d="M675 0H1200V611H888A380 380 0 0 1 675 395Z" fill="url(#photoTone)"/>
    </svg>

    <div class="brand"><span class="brand-dot"></span>Halden Praxis</div>
    <nav class="nav"><a href="#">Home</a><a href="#">Ablauf</a><a href="#">Team</a><a href="#">Kontakt</a></nav>
    <a class="btn btn-top">Termin verabreden</a>

    <h1 class="hero-title">Amerikanische<br>Chiropraktik.</h1>
    <p class="hero-sub">Endlich gibt es auch amerikanische Chiropraktik in Lindach</p>
    <a class="btn btn-main">Termin verabreden</a>
    <a class="contact-link"><span>Contact Us</span>
      <svg width="16" height="8" viewBox="0 0 16 8"><path d="M0 4H14M11 1L14.5 4L11 7" stroke="#2d2d2d" stroke-width="1.4" fill="none"/></svg>
    </a>

    <div class="social">
      <i style="left:0"></i><i style="left:67px"></i><i style="left:142px"></i>
    </div>

    <div class="hotline">
      <div class="hotline-icon">
        <svg width="18" height="18" viewBox="0 0 24 24"><path d="M6.6 3.5l2.6 3.2-1.6 2.4a12 12 0 0 0 7.3 7.3l2.4-1.6 3.2 2.6-1.5 3A16 16 0 0 1 3.6 5z" fill="none" stroke="#46b735" stroke-width="1.6" stroke-linejoin="round"/></svg>
      </div>
      <div class="hotline-label">Hotline</div>
      <div class="hotline-number">08100 5550123</div>
    </div>
  </header>

  <section class="intro">
    <h2>Chiropraktik in Lindach</h2>
    <p class="lead">Amerikanische Chiropraktik nun auch in Lindach!</p>
    <p class="body">Die Chiropraktik beschäftigt sich primär mit den Störungen des Nervensystems im Körper. Gibt es in unserem Hauptorgan (Gehirn) einen Fehler/Schwäche kann sich das in unserem Körper spiegeln! Meistens reagiert der Körper mit einer lokalen Verspannung eines Muskels. Daraus kann eine Einschränkung der</p>
  </section>
</div>
</body>
</html>
```